Quillstone Business Card

We need a business card design. We have a logo from a previous Sketchfold project and I am attaching the logo files in jpeg and photoshop.

```html
<!DOCTYPE html>
<html lang="en">
<head>
<meta charset="utf-8">
<title>Quillstone Business Card</title>
<link rel="stylesheet" href="https://fonts.googleapis.com/css2?family=Questrial&display=swap">
<style>
  :root {
    --page-bg: #f2f2f2;
    --card-dark: #4a4a4b;
    --card-light: #ffffff;
    --card-light-edge: #e4e4e4;
    --accent-green: #4cb848;
    --text-light: #ffffff;
    --text-dark: #4a4a4b;
  }
  * { margin: 0; padding: 0; box-sizing: border-box; }
  html, body {
    width: 1200px; height: 900px; overflow: hidden;
    background: var(--page-bg);
    font-family: "Questrial", "Century Gothic", sans-serif;
  }
  .business-card {
    position: absolute; left: 100px; top: 164px;
    width: 1000px; height: 571px;
    border-radius: 34px; overflow: hidden;
    box-shadow: 0 18px 40px rgba(0,0,0,0.18);
  }
  .card-background { position: absolute; inset: 0; width: 100%; height: 100%; }
  .brand-lockup {
    position: absolute; left: 62px; top: 58px;
    display: flex; align-items: center; gap: 18px;
  }
  .brand-square { width: 48px; height: 48px; background: var(--accent-green); }
  .brand-name { color: var(--text-light); font-size: 56px; line-height: 1; letter-spacing: -0.5px; }
  .holder { position: absolute; left: 62px; top: 208px; }
  .holder-name { color: var(--accent-green); font-size: 33px; line-height: 1.1; }
  .holder-role { color: var(--text-light); font-size: 22px; margin-top: 6px; }
  .contact-list {
    position: absolute; left: 62px; top: 320px;
    list-style: none; color: var(--text-light); font-size: 25px;
  }
  .contact-item { display: flex; align-items: center; gap: 12px; height: 37px; }
  .contact-item.continued { padding-left: 40px; }
  .contact-icon { width: 28px; height: 28px; fill: var(--accent-green); flex: none; }
  .feature-name {
    position: absolute; left: 712px; top: 256px; width: 240px;
    text-align: center; color: var(--text-dark); font-size: 44px;
  }
</style>
</head>
<body>
  <div class="business-card">
    <svg class="card-background" viewBox="0 0 1000 571" preserveAspectRatio="none">
      <defs>
        <radialGradient id="light-panel" cx="0.78" cy="0.45" r="0.5">
          <stop offset="0.6" stop-color="var(--card-light)"/>
          <stop offset="1" stop-color="var(--card-light-edge)"/>
        </radialGradient>
      </defs>
      <rect width="1000" height="571" fill="var(--card-dark)"/>
      <path d="M600 0 L700 0 C625 120 612 260 645 380 C575 280 560 120 600 0 Z" fill="var(--accent-green)"/>
      <path d="M665 0 L1000 0 L1000 470 C900 560 770 580 705 520 C600 430 590 170 665 0 Z" fill="url(#light-panel)"/>
    </svg>

    <div class="brand-lockup">
      <span class="brand-square"></span>
      <span class="brand-name">Quillstone</span>
    </div>

    <div class="holder">
      <p class="holder-name">Nora Pell</p>
      <p class="holder-role">Manager</p>
    </div>

    <ul class="contact-list">
      <li class="contact-item">
        <svg class="contact-icon" viewBox="0 0 24 24"><path d="M6.6 10.8a15 15 0 0 0 6.6 6.6l2.2-2.2c.3-.3.7-.4 1-.2 1.1.4 2.3.6 3.6.6.6 0 1 .4 1 1V20c0 .6-.4 1-1 1A17 17 0 0 1 3 4c0-.6.4-1 1-1h3.5c.6 0 1 .4 1 1 0 1.3.2 2.5.6 3.6.1.3 0 .7-.2 1z"/></svg>
        1800-555-0142
      </li>
      <li class="contact-item">
        <svg class="contact-icon" viewBox="0 0 24 24"><path d="M3 5h18v14H3z M4.5 6.5 12 12l7.5-5.5" fill="none" stroke="var(--accent-green)" stroke-width="2"/><path d="M3 5h18L12 12z"/></svg>
        info@quillstone.com
      </li>
      <li class="contact-item">
        <svg class="contact-icon" viewBox="0 0 24 24"><g fill="none" stroke="var(--accent-green)" stroke-width="1.8"><circle cx="12" cy="12" r="9"/><ellipse cx="12" cy="12" rx="4" ry="9"/><path d="M3 12h18M5 7h14M5 17h14"/></g></svg>
        www.quillstone.com
      </li>
      <li class="contact-item">
        <svg class="contact-icon" viewBox="0 0 24 24"><path d="M12 3 2 12h3v8h5v-5h4v5h5v-8h3z"/></svg>
        2716 Harbor Ave. Suite 410
      </li>
      <li class="contact-item continued">Coral Bay, Fl 33190</li>
    </ul>

    <p class="feature-name">Quillstone</p>
  </div>
</body>
</html>
```